Billboard - Cool Garden and Landscape Company (Brand Pack Included)

NEED A PROFESSIONAL BILLBOARD TO ADVERTISE OUR BUSINESS. HAVE MOCKED UP A SAMPLE CONCEPT BUT IT REQUIRES THE ICONS TO BE DEVELOPED TO A PROFESSIONAL STANDARD (I JUST COPIED RANDOM EXAMPLES FROM THE NET)

THE ICONS REPRESENT OUR KEY PRODUCT GROUPS. (These can be redesigned)
BILLBOARD IS 6M X 3M (SEE SPEC FILE ATTACHED) - IMAGE OF THE LOCATION ADDED TO THE FILES.

BRAND GUIDE INCLUDED WITH LOGO FILES

VISIT: https://www.facebook.com/Crew.Moss.Crate/
Web: www.mosscrate.co.nz

Target Market(s)

Commuter traffic - busy road - Billboard site is on the left side approx 400m before our street turn off. Age group 30+ Home owners / Builders

Industry/Entity Type

Garden Supply

Font styles to use
Other font styles liked:
• comfortaa

Requirements
Must have
• No change to our logo or brand
• Next left
• Icons for products as per mock up - note these can be redesigned
Nice to have
• Easy to see at a distance
• Clean
• Simple

```html
<!DOCTYPE html>
<html lang="en">
<head>
<meta charset="utf-8">
<title>MOSSCRATE Billboard</title>
<link rel="stylesheet" href="https://fonts.googleapis.com/css2?family=Comfortaa:wght@400;600;700&display=swap">
<style>
  :root {
    --orange: #f7941d;
    --orange-dark: #c9470c;
    --green: #2a9d44;
    --green-line: #1f9a3c;
    --mint: #bfe4c6;
    --ink: #1c1c1c;
    --white: #ffffff;
    --backdrop: #e9ebe8;
  }
  * { margin: 0; padding: 0; box-sizing: border-box; }
  html, body {
    width: 1200px; height: 1054px; overflow: hidden;
    background: var(--backdrop);
    font-family: "Comfortaa", sans-serif;
  }
  .billboard {
    position: absolute; left: 40px; top: 237px;
    width: 1120px; height: 580px;
    background: var(--white);
    box-shadow: 0 6px 24px rgba(0,0,0,.15);
    overflow: hidden;
  }
  .billboard-shapes { position: absolute; inset: 0; }
  .brand-mark {
    position: absolute; left: 262px; top: 42px;
    width: 88px; height: 88px; background: var(--green);
  }
  .brand-name {
    position: absolute; left: 378px; top: 50px;
    font-size: 68px; font-weight: 700; color: var(--green);
    letter-spacing: 0; line-height: 1; white-space: nowrap;
  }
  .tagline {
    position: absolute; left: 522px; top: 140px;
    font-size: 28px; line-height: 1; color: var(--orange); letter-spacing: 1px;
  }
  .products {
    position: absolute; left: 0; top: 180px; width: 1120px;
    display: flex; justify-content: space-around; padding: 0 60px;
    list-style: none;
  }
  .product { width: 220px; text-align: center; }
  .product-icon { display: block; margin: 12px auto 0; width: 146px; height: 150px; }
  .product-label { margin-top: 8px; font-size: 19px; line-height: 1.4; color: var(--ink); }
  .range-title {
    position: absolute; left: 0; width: 1120px; top: 446px;
    text-align: center; font-size: 34px; font-weight: 700; line-height: 1;
    letter-spacing: 3px; color: var(--orange);
  }
  .direction {
    position: absolute; left: 106px; top: 496px;
    font-size: 46px; font-weight: 600; line-height: 1;
    color: var(--ink); letter-spacing: 1px;
  }
  .address {
    position: absolute; left: 483px; top: 504px;
    font-size: 30px; line-height: 1; color: var(--ink);
  }
</style>
</head>
<body>
  <section class="billboard">
    <svg class="billboard-shapes" width="1120" height="580" viewBox="0 0 1120 580">
      <rect class="accent-bar" x="0" y="44" width="193" height="52" fill="var(--orange)"/>
      <path class="corner-bracket" d="M918 73 H1060 L1095 110 V205 H1043 V122 H918 Z" fill="var(--orange)"/>
      <path class="corner-bracket-shade" d="M1043 150 H1095 V205 H1043 Z" fill="var(--orange-dark)"/>
      <rect class="tagline-rule" x="237" y="156" width="276" height="4" fill="var(--orange)"/>
      <rect class="product-band" x="0" y="176" width="1120" height="256" fill="var(--mint)"/>
      <rect class="product-band-rule" x="0" y="430" width="1120" height="8" fill="var(--green-line)"/>
      <rect class="arrow-band-shade" x="1040" y="438" width="50" height="60" fill="var(--orange-dark)"/>
      <path class="arrow-band" d="M20 519 L80 464 V490 H1112 L1062 548 H80 V574 Z" fill="var(--orange)"/>
    </svg>

    <span class="brand-mark"></span>
    <h1 class="brand-name">MOSSCRATE</h1>
    <p class="tagline">Create Better Gardens</p>

    <ul class="products">
      <li class="product">
        <svg class="product-icon" viewBox="0 0 146 150" role="img" aria-label="Firewood and flame icon">
          <path d="M73 4 L140 34 V100 L73 146 L6 100 V34 Z" fill="var(--white)" stroke="var(--green)" stroke-width="4"/>
          <circle cx="73" cy="75" r="38" fill="#2b2b2b"/>
        </svg>
        <p class="product-label">Firewood<br>Fire Pellets</p>
      </li>
      <li class="product">
        <svg class="product-icon" viewBox="0 0 146 150" role="img" aria-label="Seedling in soil icon">
          <path d="M73 4 L140 34 V100 L73 146 L6 100 V34 Z" fill="var(--white)" stroke="var(--green)" stroke-width="4"/>
          <circle cx="73" cy="75" r="38" fill="#2b2b2b"/>
        </svg>
        <p class="product-label">Compost<br>Soil + Mulch</p>
      </li>
      <li class="product">
        <svg class="product-icon" viewBox="0 0 146 150" role="img" aria-label="Stacked stones icon">
          <path d="M73 4 L140 34 V100 L73 146 L6 100 V34 Z" fill="var(--white)" stroke="var(--green)" stroke-width="4"/>
          <circle cx="73" cy="75" r="38" fill="#2b2b2b"/>
        </svg>
        <p class="product-label">Decorative Stone<br>Aggregates</p>
      </li>
      <li class="product">
        <svg class="product-icon" viewBox="0 0 146 150" role="img" aria-label="Box trailer icon">
          <path d="M73 4 L140 34 V100 L73 146 L6 100 V34 Z" fill="var(--white)" stroke="var(--green)" stroke-width="4"/>
          <circle cx="73" cy="75" r="38" fill="#2b2b2b"/>
        </svg>
        <p class="product-label">Hire Trailers<br>Delivery</p>
      </li>
    </ul>

    <h2 class="range-title">Garden &amp; Landscape Supplies</h2>
    <p class="direction">NEXT LEFT</p>
    <p class="address">42 Tarlow Road (off Brenmore)</p>
  </section>
</body>
</html>
```